Pellow CCTV A5 Flyer for attracting sales

Looking for an A5 flyer to be designed to advertise 3 specific CCTV packages from my website www.pellowcctv-demo.com. the packages are I - 3 camera solution J - 4 cameras and L - 5 cameras. The background of the flyer should be white as I will be printing these myself on standard white A5 paper. Need to advertise also the business contact details and for it to say somewhere "protect your home with our CCTV packages". Also need to get the message across that we supply and install as well as there being a 1 year onsite warranty with all our packages. If you feel A5 is not big enough then feel free to design on A4
Industry/Entity Type
Security Service
Look and feel
Each slider illustrates characteristics of the customer's brand and the style your logo design should communicate.

```html
<!DOCTYPE html>
<html lang="en">
<head>
<meta charset="utf-8">
<title>Pellow CCTV – A5 Flyer</title>
<link href="https://fonts.googleapis.com/css2?family=Open+Sans:wght@400;600;700;800&family=Signika:wght@600;700&display=swap" rel="stylesheet">
<style>
:root{
  --page-bg:#e6e6e6;
  --paper:#ffffff;
  --red:#a3161b;
  --ink:#222222;
  --navy:#0a4fa0;
  --sky:#1aa3e8;
  --panel:#f1f1f1;
  --footer-tint:#cfeaf9;
  --footer-bar:#0b5aa8;
}
*{margin:0;padding:0;box-sizing:border-box}
html,body{width:1200px;height:1200px;overflow:hidden;background:var(--page-bg)}
body{font-family:"Open Sans",sans-serif;color:var(--ink)}
.flyer{position:absolute;left:210px;top:48px;width:780px;height:1104px;background:var(--paper);overflow:hidden;box-shadow:0 4px 18px rgba(0,0,0,.18)}
.hero{position:absolute;left:0;top:0;width:780px;height:355px}
.photo{position:absolute}
.photo-a{left:0;top:0;width:258px;height:158px;background:linear-gradient(135deg,#a99a90,#d9d3cc 60%,#8c7f78)}
.photo-b{left:262px;top:0;width:518px;height:158px;background:linear-gradient(120deg,#dfe6ee,#c8d3e0 55%,#eef1f4)}
.photo-c{left:0;top:162px;width:258px;height:150px;background:linear-gradient(120deg,#c86aa5,#e6c97a 55%,#c9c1ba)}
.photo-d{left:262px;top:162px;width:518px;height:193px;background:linear-gradient(120deg,#c9cfe0,#e8e3dc 50%,#d6dde8)}
.camera{position:absolute;left:455px;top:20px;width:300px;height:300px;border-radius:50%;background:radial-gradient(circle at 45% 40%,#ffffff,#e3e5e8 55%,#b9bdc3)}
.brand-mark{position:absolute;left:60px;top:118px;display:flex;align-items:center;gap:10px;background:rgba(255,255,255,.55);padding:4px 10px}
.brand-mark .dot{width:22px;height:22px;border-radius:50%;background:#111}
.brand-mark span{font-weight:800;font-size:32px;color:#111;letter-spacing:-.5px}
.stripes{position:absolute;left:0;top:290px}
.headline{position:absolute;left:28px;top:352px;font-family:"Signika",sans-serif;color:var(--red);line-height:1}
.headline h1{font-size:46px;font-weight:700}
.headline h2{font-size:33px;font-weight:700;margin-top:2px}
.intro{position:absolute;left:30px;top:432px;width:740px;font-size:22.5px;line-height:25px;color:#222}
.packages{position:absolute;left:19px;top:498px;display:flex;gap:11px}
.package{width:239px;height:384px;background:var(--panel)}
.package h3{font-size:16.5px;font-weight:700;color:var(--red);text-align:center;line-height:23px;padding-top:10px;height:58px;background:#f6f6f6}
.pkg-brand{display:flex;align-items:center;gap:8px;padding:10px 0 0 12px}
.pkg-brand .dot{width:18px;height:18px;border-radius:50%;background:#111}
.pkg-brand span{font-weight:800;font-size:21px;color:#111}
.pkg-maker{display:flex;align-items:center;gap:20px;padding:2px 0 0 62px}
.pkg-maker span{font-weight:700;font-size:19px;color:var(--red)}
.pkg-maker .badge{width:30px;height:26px;background:#e0a21c;border:2px solid #333}
.kit{margin:6px auto 0;width:192px;height:64px;background:linear-gradient(180deg,#e9ebee 0,#e9ebee 55%,#3c4048 60%,#5a5f68 100%)}
.specs{list-style:none;padding:14px 8px 0 10px;font-size:14.5px;line-height:16.5px;color:#333}
.specs li{position:relative;padding-left:18px;margin-bottom:4px}
.specs li::before{content:"";position:absolute;left:0;top:5px;width:6px;height:6px;border:1.5px solid var(--navy);border-radius:50%}
.contact-zone{position:absolute;left:0;top:895px;width:780px;height:160px;background:var(--footer-tint)}
.contact-stripes{position:absolute;left:0;top:0}
.contact{position:absolute;left:38px;top:55px;font-size:15px;line-height:18px;font-style:normal}
.contact strong{display:block;font-size:15px;padding-left:24px;margin-bottom:2px}
.contact .row{display:flex;gap:10px;align-items:flex-start}
.contact svg{flex:none;margin-top:3px}
.payments{position:absolute;left:270px;top:88px;width:232px;height:56px;border:1px solid #8fb3d9;background:#fff}
.payments .wallet{position:absolute;left:12px;top:-10px;background:var(--footer-tint);padding:0 4px;font-weight:700;font-size:14px;color:var(--navy)}
.cards{position:absolute;left:6px;top:14px;display:flex;gap:5px}
.cards span{width:50px;height:32px;display:flex;align-items:center;justify-content:center;font-size:10.5px;font-weight:700;color:#fff;background:var(--navy)}
.hours{position:absolute;right:32px;top:74px;text-align:right;font-size:15px;line-height:16.5px}
.footer-bar{position:absolute;left:0;top:1055px;width:780px;height:49px;background:var(--footer-bar);color:#fff;font-size:15px;display:flex;align-items:center;justify-content:space-between;padding:0 32px 0 37px}
.footer-bar .web{display:flex;align-items:center;gap:10px}
</style>
</head>
<body>
<main class="flyer">
  <section class="hero">
    <div class="photo photo-a" role="img" aria-label="Photo of a cosy living room with armchair and cushions"></div>
    <div class="photo photo-b" role="img" aria-label="Photo of a bright bedroom with white bedding"></div>
    <div class="photo photo-c" role="img" aria-label="Photo of colourful armchairs in a lounge"></div>
    <div class="photo photo-d" role="img" aria-label="Photo of a pastel living room with sofa"></div>
    <div class="camera" role="img" aria-label="Photo of a white dome security camera"></div>
    <div class="brand-mark"><i class="dot"></i><span>Pellow CCTV Ltd</span></div>
    <svg class="stripes" width="780" height="80" viewBox="0 0 780 80">
      <polygon points="0,5 780,52 780,62 690,70 0,26" fill="var(--navy)"/>
      <polygon points="0,30 580,70 570,78 0,40" fill="var(--sky)"/>
    </svg>
  </section>

  <header class="headline">
    <h1>Protect Your Home</h1>
    <h2>With Our CCTV Packages</h2>
  </header>
  <p class="intro">We supply and install as well as there being a 1 year onsite warranty with all our packages.</p>

  <section class="packages">
    <article class="package">
      <h3>[Package I 1080P] 3 Camera<br>CCTV Package Installation</h3>
      <div class="pkg-brand"><i class="dot"></i><span>Pellow CCTV Ltd</span></div>
      <div class="pkg-maker"><span>Vantera</span><i class="badge"></i></div>
      <div class="kit" role="img" aria-label="Three dome cameras above a recorder unit"></div>
      <ul class="specs">
        <li>DVR Recording Resolution 1920x1080 Full HD 1080p</li>
        <li>4 Channel 1080p DVR</li>
        <li>High quality 1080p Cameras with 40m IR Distance</li>
        <li>2TB hard drive</li>
        <li>HDMI / VGA Ports</li>
        <li>Remote video footage access via a mobile app</li>
      </ul>
    </article>
    <article class="package">
      <h3>[Package J 1080P] 4 Camera<br>CCTV Package Installation</h3>
      <div class="pkg-brand"><i class="dot"></i><span>Pellow CCTV Ltd</span></div>
      <div class="pkg-maker"><span>Vantera</span><i class="badge"></i></div>
      <div class="kit" role="img" aria-label="Four dome cameras above a recorder unit"></div>
      <ul class="specs">
        <li>DVR Recording Resolution 1920x1080 Full HD 1080p</li>
        <li>4 Channel 1080p DVR</li>
        <li>High quality 1080p Cameras with 40m IR Distance</li>
        <li>2TB hard drive</li>
        <li>HDMI / VGA Ports</li>
        <li>Remote video footage access via a mobile app</li>
      </ul>
    </article>
    <article class="package">
      <h3>[Package L 1080P] 5 Camera<br>CCTV Package Installation</h3>
      <div class="pkg-brand"><i class="dot"></i><span>Pellow CCTV Ltd</span></div>
      <div class="pkg-maker"><span>Vantera</span><i class="badge"></i></div>
      <div class="kit" role="img" aria-label="Five dome cameras above a recorder unit"></div>
      <ul class="specs">
        <li>DVR Recording Resolution 1920x1080 Full HD 1080p</li>
        <li>8 Channel 1080p DVR</li>
        <li>High quality 1080p Cameras with 40m IR Distance</li>
        <li>3TB hard drive</li>
        <li>HDMI / VGA Ports</li>
        <li>Remote video footage access via a mobile app</li>
      </ul>
    </article>
  </section>

  <section class="contact-zone">
    <svg class="contact-stripes" width="780" height="70" viewBox="0 0 780 70">
      <polygon points="0,0 780,0 780,40 220,12 210,0" fill="var(--paper)"/>
      <polygon points="220,10 780,50 780,62 240,16" fill="var(--navy)"/>
      <polygon points="350,8 780,42 780,48 345,12" fill="var(--sky)"/>
    </svg>
    <address class="contact">
      <strong>Pellow CCTV Ltd</strong>
      <div class="row"><svg width="14" height="14" viewBox="0 0 14 14"><path d="M7 1a4 4 0 0 0-4 4c0 3 4 8 4 8s4-5 4-8a4 4 0 0 0-4-4z" fill="none" stroke="#b33" stroke-width="1.3"/><circle cx="7" cy="5" r="1.3" fill="#b33"/></svg><span>14 Harrow Lane<br>London E2 4QX</span></div>
      <div class="row"><svg width="14" height="14" viewBox="0 0 14 14"><rect x="1" y="3" width="12" height="8" fill="none" stroke="#b33" stroke-width="1.2"/><path d="M1 3l6 5 6-5" fill="none" stroke="#b33" stroke-width="1.2"/></svg><span>info@pellowcctv-demo.com</span></div>
      <div class="row"><svg width="14" height="14" viewBox="0 0 14 14"><circle cx="7" cy="7" r="6" fill="none" stroke="#b33" stroke-width="1.2"/><path d="M5 4l1.5 2-1 1 2 2 1-1 2 1.5-1 1.5C7 11 3.5 7.5 4 5z" fill="#b33"/></svg><span>+44 (0)20 7946 0321</span></div>
    </address>
    <div class="payments">
      <span class="wallet">Nuvipay</span>
      <div class="cards"><span>Vorelo</span><span>Cardix</span><span>Zentrik</span><span>Orbinex</span></div>
    </div>
    <div class="hours">
      OPENING HOURS<br>
      Mon - Fri: 9:30am - 5pm<br>
      Saturday: 9:30am - 5pm<br>
      Sunday: 10am - 4pm
    </div>
  </section>

  <footer class="footer-bar">
    <span>UK Registered Company: 12345678</span>
    <span class="web"><svg width="11" height="11" viewBox="0 0 12 12"><circle cx="6" cy="6" r="5" fill="none" stroke="#fff" stroke-width="1"/><path d="M1 6h10M6 1c2 2 2 8 0 10M6 1c-2 2-2 8 0 10" fill="none" stroke="#fff" stroke-width="1"/></svg>www.pellowcctv-demo.com</span>
  </footer>
</main>
</body>
</html>
```